Redesign screen for Savings Mobile App

We need a resign of our whole app. This time, we are offering the redesign of one of the screens to see all your potential. Our intention later is to do the whole app, plus corporate web site, brochures, business cards, etc. So yes there is more to work on in the near future.
Let me share some details about what the app does and is it about:
-Focused on customer fidelity to small and medium businesses.
-The app lets the customers win free samples, discounts, gifts on the store that they like. Money savings basically.
-It will be mostly used by young users (female and male) around 18 to 40 years old.
-The app focus on get free discounts, gifts as free coffees, ice-creams, etc.
-Will use a lot of plivora in terms of announcements, sharing and more.

So the design should look fresh and funny. This is an hybrid html5/css3 android app. Our focus is now Android so please make sure to follow http://www.vantrelo.com/design/

The attached screenshot is a sample of the working app that we have now. Notice that it lacks of design, it is basically just a raw design of the controls that we needed in place. That is why we need your creativity.

Here we are looking for basically 2 new redesigns:
1 - The screen per se.
2 - The fortune wheel. I attached a screenshot of one that I like. Of course it should not be the same but follow the same idea.

Industry/Entity Type

Store

Font styles to use
Other font styles liked:
• Signika

Requirements
Must have
• Fresh and Funny design
Should not have
• Dark and negative colors

```html
<!DOCTYPE html>
<html lang="es">
<head>
<meta charset="utf-8">
<title>Cafe Lumora – Ruleta</title>
<link href="https://fonts.googleapis.com/css2?family=Open+Sans:wght@300;400;600&display=swap" rel="stylesheet">
<style>
  :root {
    --bg-deep: #f7902f;
    --bg-warm: #fba94a;
    --bg-light: #fdd27a;
    --text-light: #fff8ee;
    --brand-red: #a8171f;
    --brand-dark: #5a2a12;
    --button: #f4743f;
    --button-shadow: #d95a2a;
    --ring: #fbb33e;
    --hub: #f2f2f2;
  }
  html, body {
    margin: 0;
    padding: 0;
    width: 786px;
    height: 1200px;
    overflow: hidden;
    background: var(--bg-deep);
  }
  .screen {
    position: relative;
    width: 786px;
    height: 1200px;
    overflow: hidden;
    font-family: "Open Sans", sans-serif;
    color: var(--text-light);
    background:
      radial-gradient(circle at 78% 58%, var(--bg-light) 0%, rgba(253,210,122,0) 45%),
      radial-gradient(circle at 20% 45%, rgba(255,230,170,0.45) 0%, rgba(255,230,170,0) 30%),
      linear-gradient(180deg, var(--bg-deep) 0%, var(--bg-warm) 55%, var(--bg-deep) 100%);
  }
  .welcome-title {
    position: absolute;
    top: 60px;
    left: 0;
    width: 100%;
    margin: 0;
    text-align: center;
    font-size: 30px;
    font-weight: 400;
  }
  .welcome-text {
    position: absolute;
    top: 126px;
    left: 100px;
    width: 586px;
    margin: 0;
    text-align: center;
    font-size: 20px;
    font-weight: 300;
    line-height: 26px;
  }
  .brand {
    position: absolute;
    top: 245px;
    left: 0;
    width: 100%;
    display: flex;
    justify-content: center;
    align-items: center;
    gap: 10px;
  }
  .brand-dot {
    width: 22px;
    height: 22px;
    border-radius: 50%;
    background: var(--brand-red);
  }
  .brand-name {
    font-size: 30px;
    font-weight: 600;
    color: var(--brand-red);
  }
  .wheel {
    position: absolute;
    left: 86px;
    top: 379px;
    width: 600px;
    height: 600px;
  }
  .spin-button {
    position: absolute;
    left: 145px;
    top: 1022px;
    width: 484px;
    height: 75px;
    border: none;
    border-radius: 7px;
    background: var(--button);
    box-shadow: 0 3px 0 var(--button-shadow);
    color: #fff;
    font-family: "Open Sans", sans-serif;
    font-size: 28px;
    font-weight: 400;
  }
</style>
</head>
<body>
<main class="screen">
  <h1 class="welcome-title">Welcome to Cafe Lumora!</h1>
  <p class="welcome-text">Lorem ipsum dolor sit amet, accusata adipiscing cused eam purto quodsi efficiantur.</p>

  <div class="brand">
    <span class="brand-dot"></span>
    <span class="brand-name">cafe lumora</span>
  </div>

  <svg class="wheel" viewBox="-300 -300 600 600" role="img" aria-label="Prize wheel with ten coloured segments">
    <defs>
      <radialGradient id="hubShade" cx="45%" cy="40%" r="60%">
        <stop offset="0%" stop-color="#ffffff"/>
        <stop offset="100%" stop-color="#dcdcdc"/>
      </radialGradient>
    </defs>
    <circle r="292" fill="var(--ring)" opacity="0.55"/>
    <circle r="282" fill="#fff"/>
    <g stroke="#fff" stroke-width="3">
      <path d="M0 0 L0 -275 A275 275 0 0 1 161.6 -222.5 Z" fill="#3cc7a8"/>
      <path d="M0 0 L161.6 -222.5 A275 275 0 0 1 261.6 -85 Z" fill="#6fdc55"/>
      <path d="M0 0 L261.6 -85 A275 275 0 0 1 261.6 85 Z" fill="#f9c8f0"/>
      <path d="M0 0 L261.6 85 A275 275 0 0 1 161.6 222.5 Z" fill="#f3e03c"/>
      <path d="M0 0 L161.6 222.5 A275 275 0 0 1 0 275 Z" fill="#f39a5e"/>
      <path d="M0 0 L0 275 A275 275 0 0 1 -161.6 222.5 Z" fill="#e0657d"/>
      <path d="M0 0 L-161.6 222.5 A275 275 0 0 1 -261.6 85 Z" fill="#7b8fd6"/>
      <path d="M0 0 L-261.6 85 A275 275 0 0 1 -261.6 -85 Z" fill="#0fc7c7"/>
      <path d="M0 0 L-261.6 -85 A275 275 0 0 1 -161.6 -222.5 Z" fill="#3a8ee0"/>
      <path d="M0 0 L-161.6 -222.5 A275 275 0 0 1 0 -275 Z" fill="#5b4fb8"/>
    </g>
    <circle r="60" fill="url(#hubShade)"/>
    <path d="M-14 -50 L0 -82 L14 -50 Z" fill="url(#hubShade)"/>
    <line x1="0" y1="-80" x2="0" y2="-30" stroke="#cfcfcf" stroke-width="2"/>
  </svg>

  <button class="spin-button">Girar la ruleta ahora!!!</button>
</main>
</body>
</html>
```